Olive oil bottle labels, front and back.

Sophisticated uncluttered distinctive eye catching label
Front label:
Label on front like the uploaded file in design but called “Corrowick Hollow”, (not Marrabel Reach.)
Need to state that it’s extra virgin, cold pressed olive oil, 100% organic, grown and pressed on the Mornington Peninsula.
500 ml
Back label:
Nutritional information table (see label example in uploaded files) including FFA 0.1% Oleic Acid
Storage: airtight in cool dark place
Made and produced in Australia from 100% Australian ingredients,
Harvest date:
Best by:
Batch:
Grown, harvested and bottled at The Hollow, Pellandry Rd. Flinders. 3847
The back label on uploaded files has the info requited except they should have address and don't include those industry and Australian made logos.
The front label is what we want, first to plagiarise without copyright infringement gets the gig, thanks.
Labels front and back need be 5 x 13 cm
Gourmet, up-market
- Love "Adorn Regular Garland"

```html
<!DOCTYPE html>
<html lang="en">
<head>
<meta charset="utf-8">
<title>Corrowick Hollow Extra Virgin Olive Oil – Bottle Labels</title>
<link rel="stylesheet" href="https://fonts.googleapis.com/css2?family=Oswald:wght@300;400&family=Questrial&display=swap">
<style>
  :root {
    --page: #ffffff;
    --label-black: #05050a;
    --ink-white: #f2f2f2;
    --gold: #a8853f;
    --gold-light: #d7b870;
    --gold-deep: #7a5a22;
    --ghost: #0e0e14;
  }
  * { margin: 0; padding: 0; box-sizing: border-box; }
  html, body { width: 1200px; height: 1000px; overflow: hidden; background: var(--page); }
  .canvas { position: relative; width: 1200px; height: 1000px; }

  .label {
    position: absolute;
    width: 372px;
    height: 967px;
    background: var(--label-black);
    overflow: hidden;
    font-family: "Oswald", "Arial Narrow", sans-serif;
    font-weight: 300;
    color: var(--ink-white);
  }
  .label--front { left: 207px; top: 17px; }
  .label--back  { left: 627px; top: 16px; }

  .abs { position: absolute; }
  .centered { left: 0; width: 100%; text-align: center; }

  /* Front */
  .product-type { left: 130px; width: 214px; text-align: center; font-family: "Questrial", sans-serif; }
  .product-type__grade { top: 125px; font-size: 21px; letter-spacing: 1px; color: var(--ink-white); }
  .product-type__name {
    top: 146px; font-size: 38px;
    background: linear-gradient(90deg, var(--gold-deep), var(--gold-light) 55%, var(--gold));
    -webkit-background-clip: text; background-clip: text; color: transparent;
  }
  .branch-art {
    left: 146px; top: 212px; width: 226px; height: 500px;
    background: radial-gradient(ellipse at 70% 50%, rgba(168,133,63,0.22), rgba(168,133,63,0.04) 70%, transparent 80%);
  }
  .brand-name {
    top: 728px; font-family: "Questrial", sans-serif; font-size: 36px;
    color: var(--gold); letter-spacing: 0.5px;
  }
  .drop { display: block; margin: 0 auto; }
  .front-drop { top: 812px; }
  .front-specs { top: 842px; font-size: 13px; line-height: 19.5px; }
  .front-specs .gold { color: var(--gold); }
  .front-origin { top: 910px; font-size: 12.5px; color: var(--gold); letter-spacing: 0.2px; }

  /* Back */
  .ghost-art {
    left: 0; top: 60px; width: 372px; height: 760px;
    background: radial-gradient(ellipse at 55% 45%, var(--ghost), transparent 70%);
  }
  .nutrition-title { left: 54px; top: 110px; font-size: 17px; }
  .nutrition-table { left: 54px; top: 166px; width: 210px; border-collapse: collapse; font-size: 16px; }
  .nutrition-table td { height: 26.2px; padding: 0; white-space: nowrap; vertical-align: middle; }
  .nutrition-table .per-serve { width: 40px; }
  .nutrition-table .per-100 { text-align: right; }
  .nutrition-table .indent { padding-left: 12px; }
  .storage { left: 53px; top: 536px; font-size: 16px; }
  .back-drop { top: 630px; }
  .made-in { top: 685px; font-size: 17px; line-height: 23px; color: var(--gold); }
  .grown-at { top: 803px; font-size: 12.5px; line-height: 18px; }
  .batch-details { left: 85px; top: 871px; width: 198px; font-size: 12px; line-height: 18.5px; }
  .batch-details div { display: flex; justify-content: space-between; }
</style>
</head>
<body>
<div class="canvas">

  <section class="label label--front" aria-label="Front label">
    <div class="abs product-type product-type__grade">EXTRA VIRGIN</div>
    <div class="abs product-type product-type__name">Olive Oil</div>
    <div class="abs branch-art" role="img" aria-label="Gold line illustration of an olive branch with leaves and olives"></div>
    <div class="abs centered brand-name">Corrowick Hollow</div>
    <svg class="abs centered front-drop drop" width="14" height="22" viewBox="0 0 14 22" aria-hidden="true">
      <defs><linearGradient id="dropGoldA" x1="0" y1="0" x2="1" y2="1"><stop offset="0" stop-color="#d7b870"/><stop offset="1" stop-color="#7a5a22"/></linearGradient></defs>
      <path d="M7 0 C9 6 14 11 14 15 A7 7 0 0 1 0 15 C0 11 5 6 7 0 Z" fill="url(#dropGoldA)"/>
    </svg>
    <div class="abs centered front-specs">
      500 ML<br>COLD PRESSED<br><span class="gold">100% ORGANIC</span>
    </div>
    <div class="abs centered front-origin">GROWN ON THE MORNINGTON PENINSULA</div>
  </section>

  <section class="label label--back" aria-label="Back label">
    <div class="abs ghost-art" role="img" aria-label="Faint olive branch line illustration in the background"></div>
    <div class="abs nutrition-title">NUTRITIONAL INFORMATION TABLE</div>
    <table class="abs nutrition-table">
      <tr><td>&nbsp;AVG QTY</td><td class="per-serve">PER</td><td>&nbsp;PER</td></tr>
      <tr><td></td><td class="per-serve">15ML</td><td class="per-100">100ML</td></tr>
      <tr><td>ENRGY (KJ)</td><td class="per-serve">571</td><td class="per-100">3446</td></tr>
      <tr><td>PROTEIN (G)</td><td class="per-serve">0</td><td class="per-100">0</td></tr>
      <tr><td>FAT (G)</td><td class="per-serve"></td><td></td></tr>
      <tr><td class="indent">TOTAL</td><td class="per-serve">13.7</td><td class="per-100">91.5</td></tr>
      <tr><td class="indent">SATURED</td><td class="per-serve">2.1</td><td class="per-100">14.1</td></tr>
      <tr><td class="indent">MONOSATURATED</td><td class="per-serve">10.7</td><td class="per-100">71.5</td></tr>
      <tr><td class="indent">POLYUNSATURATED</td><td class="per-serve">0.9</td><td class="per-100">5.9</td></tr>
      <tr><td class="indent">TRASN FATTY ACID</td><td class="per-serve">&lt;0.01</td><td class="per-100">&lt;0.05</td></tr>
      <tr><td>CHOLESTEROL (MG)</td><td class="per-serve">0</td><td class="per-100">0</td></tr>
      <tr><td>CARBOHYDRATE (G)</td><td class="per-serve">0</td><td class="per-100">0</td></tr>
      <tr><td class="indent">SUGAR (G)</td><td class="per-serve">0</td><td class="per-100">0</td></tr>
    </table>
    <div class="abs storage">STORAGE: AIRTIGHT IN COOL DARK PLACE</div>
    <svg class="abs centered back-drop drop" width="26" height="40" viewBox="0 0 14 22" aria-hidden="true">
      <defs><linearGradient id="dropGoldB" x1="0" y1="0" x2="1" y2="1"><stop offset="0" stop-color="#d7b870"/><stop offset="1" stop-color="#7a5a22"/></linearGradient></defs>
      <path d="M7 0 C9 6 14 11 14 15 A7 7 0 0 1 0 15 C0 11 5 6 7 0 Z" fill="url(#dropGoldB)"/>
    </svg>
    <div class="abs centered made-in">MADE AND PRODUCED IN AUSTRALIA<br>FROM 100% AUSTRALIAN INGREDIENTS</div>
    <div class="abs centered grown-at">GROWN, HARVESTED AND BOTTLED<br>AT THE HOLLOW, PELLANDRY RD. FLINDERS. 3847</div>
    <div class="abs batch-details">
      <div><span>HARVEST DATE:</span><span>DECEMBER 2022</span></div>
      <div><span>BEST BY:</span><span>DECEMBER 2023</span></div>
      <div><span>FFA</span><span>0.1%&nbsp;&nbsp;OLEIC ACID</span></div>
      <div><span>BATCH:</span><span>00012358</span></div>
    </div>
  </section>

</div>
</body>
</html>
```